National Sales & Merchandising Company Needs a PowerPoint design

We need a professional PowerPoint template designed for our Sydney based National Sales & Merchandising Company. We provide sales representatives and merchandisers to companies working in the FMCG space, such as Fizzmont, Larkwells, Dorvan's, Kelmor (Vitalux Pop N Sip) and Brulo (Morning Press). We would like someone to use the colours/ design elements from our website (www.brightlanereps.com.au). We require a couple of different PPT templates with white backgrounds (e.g. first slide, new section slide, using an interesting new bullet point style, table and chart friendly and with space for headers and footers. We want a clean but dynamic look.
Reason: Hi designers,
Hoping to see some fluid lines around the outside of the slides, not coloured boxes that I could create myself. White background is required too.
Please see our website for ideas.
Thanks,
Mira
It Company

```html
<!DOCTYPE html>
<html lang="en">
<head>
<meta charset="utf-8">
<title>New Section Slide</title>
<link rel="stylesheet" href="https://fonts.googleapis.com/css2?family=Archivo+Black&family=Open+Sans:wght@400&display=swap">
<style>
  :root {
    --navy: #1f3864;
    --gold-rule: #f0b323;
    --ink: #111111;
    --paper: #ffffff;
    --light-deep: #1c3f7a;
    --light-amber: #f3a41c;
    --light-glow: #fde9a8;
    --light-bronze: #b8741a;
  }
  html, body {
    margin: 0;
    padding: 0;
    width: 1200px;
    height: 900px;
    overflow: hidden;
    background: var(--paper);
  }
  .slide {
    position: relative;
    width: 1200px;
    height: 900px;
    background: var(--paper);
    overflow: hidden;
  }
  .light-trail-strip {
    position: absolute;
    top: 0;
    right: 0;
    width: 155px;
    height: 900px;
    background: linear-gradient(180deg,
      var(--light-deep) 0%,
      #3b4f7c 10%,
      var(--light-amber) 22%,
      #e35a12 32%,
      var(--light-glow) 42%,
      #ffffff 48%,
      var(--light-amber) 56%,
      var(--light-glow) 64%,
      #e8a532 76%,
      var(--light-bronze) 100%);
  }
  .section-title {
    position: absolute;
    left: 95px;
    top: 488px;
    margin: 0;
    font-family: "Archivo Black", "Arial Black", sans-serif;
    font-size: 84px;
    line-height: 1;
    letter-spacing: 1px;
    color: var(--navy);
    white-space: nowrap;
  }
  .title-rule {
    position: absolute;
    left: 90px;
    top: 588px;
    width: 929px;
    height: 2px;
    background: var(--gold-rule);
  }
  .section-subtitle {
    position: absolute;
    left: 94px;
    top: 608px;
    margin: 0;
    font-family: "Open Sans", "Calibri", sans-serif;
    font-size: 33px;
    line-height: 1.2;
    color: var(--ink);
  }
</style>
</head>
<body>
  <main class="slide">
    <div class="light-trail-strip" role="img" aria-label="Long-exposure photograph of streaking amber and blue light trails"></div>
    <h1 class="section-title">New Section Slide</h1>
    <div class="title-rule"></div>
    <p class="section-subtitle">Add your subtitle here</p>
  </main>
</body>
</html>
```